Wordpress Website - for cutting edge Artificial Intelligence company

We need a wordpress web site for our company Varnolix.

Objective:
- To promote our software products to potential customers (e.g. large corporations)
- To promote our software products to potential partners (e.g. software makers who want to bundle our software inside their products)
- To promote our company to potential Investors (venture capital funds, angel investors, etc.)

Sample content and proposed structure can be found in the attached file.
Company logo is also attached.

The Quillet logo should only be used in the section relating to the Quillet Product (e.g. Quillet Text & Quillet Speech)

Target Market(s)

Core Target Market:
- Large corporations (e.g. Major Banks, Retailers & Pharmaceutical companies) who could buy our software

Industry/Entity Type

Software

Coding

Coded - Design and coding required

Font styles to use
Sans Serif

Colors
ffffff
ec1f27
000000
757575
dfdfdf
9bcb3c

Requirements
Must have
• Functionality:
• - Designed in Wordpress (using tools from wordpress.org, not hosted on wordpress.com)
• - Must have a user friendly CMS module for us to make updates easily
• - Must be designed to look great across different devices
• - Must be designed to look great in English and Chinese (as well as other future languages).

```html
<!DOCTYPE html>
<html lang="en">
<head>
<meta charset="utf-8">
<title>Varnolix</title>
<link rel="stylesheet" href="https://fonts.googleapis.com/css2?family=Open+Sans:wght@300;400;600;700&display=swap">
<style>
:root{
  --red:#ec1f27;
  --black:#000000;
  --ink:#222222;
  --grey:#757575;
  --light:#dfdfdf;
  --paper:#ffffff;
  --green:#9bcb3c;
  --dark:#231f20;
  --caption:rgba(25,25,25,.88);
}
*{box-sizing:border-box;margin:0;padding:0}
html,body{width:1200px;height:2980px;overflow:hidden}
body{position:relative;background:var(--paper);font-family:"Open Sans",Arial,sans-serif;color:var(--ink)}
.abs{position:absolute}

/* header */
.site-header{position:absolute;left:0;top:0;width:1200px;height:80px;background:var(--paper)}
.brand{position:absolute;left:154px;top:20px;font-size:34px;font-weight:700;color:var(--red);letter-spacing:1px;line-height:40px}
.main-nav{position:absolute;left:422px;top:30px;display:flex;gap:30px;font-size:13px;color:var(--ink)}
.main-nav .active{color:var(--red)}
.lang{position:absolute;left:954px;top:30px;font-size:13px;display:flex;align-items:center;gap:6px}
.submenu{position:absolute;left:550px;top:80px;width:206px;height:108px;background:var(--paper);box-shadow:0 3px 8px rgba(0,0,0,.25);z-index:5;font-size:11px;color:var(--grey)}
.submenu div{height:54px;line-height:54px;padding-left:16px}
.submenu div+div{border-top:1px solid var(--light);margin:0 14px;padding-left:2px}

/* hero */
.hero{position:absolute;left:0;top:80px;width:1200px;height:440px;background:linear-gradient(100deg,#6f6a68 0%,#a49c97 35%,#8b817b 60%,#4b4542 100%)}
.hero-strip{position:absolute;left:0;top:0;width:1200px;height:30px;background:rgba(40,40,40,.75);color:var(--green);font-size:11px;font-weight:600;line-height:30px;padding-left:154px}
.hero-title{position:absolute;left:0;top:158px;width:1200px;text-align:center;color:var(--paper);font-size:29px;font-weight:300;line-height:40px}
.hero-actions{position:absolute;left:0;top:374px;width:1200px;height:66px;display:flex;background:rgba(45,45,45,.85)}
.hero-actions .action{flex:0 0 auto;display:flex;align-items:center;justify-content:center;gap:18px;color:var(--paper);font-size:12px;font-weight:600;letter-spacing:.5px}
.action.demo{width:450px;border-left:1px solid rgba(255,255,255,.15);margin-left:0}
.action.contact{width:306px;background:var(--red)}
.action.partners{width:444px}

/* section titles */
.section-title{position:absolute;left:0;width:1200px;display:flex;justify-content:center;align-items:center;gap:22px;font-size:20px;font-weight:600;color:var(--black)}
.section-title::before,.section-title::after{content:"";width:130px;height:1px;background:#9a9a9a}
.section-title .brand-word{color:var(--red);font-weight:600;letter-spacing:1px}

/* news tiles */
.tile{position:absolute;overflow:hidden;background:linear-gradient(135deg,#8d8d8d,#5e5e5e)}
.tile .art{position:absolute;inset:0}
.tile .big{position:absolute;color:var(--paper);font-weight:300;line-height:1}
.tile .caption{position:absolute;left:0;bottom:0;width:100%;height:66px;background:var(--caption);color:var(--paper);font-size:12px;font-weight:700;line-height:16px;padding:16px 60px 0 20px}
.tile .more{position:absolute;right:18px;bottom:18px}
.tile.feature{background:var(--black);color:var(--paper);padding:22px 18px}
.feature h3{font-size:17px;font-weight:400;line-height:24px}
.feature p{font-size:12px;line-height:20px;margin-top:16px;color:#ddd}
.feature .cta{position:absolute;left:20px;bottom:20px;display:flex;align-items:center;gap:12px;color:var(--red);font-size:12px;font-weight:600}

/* testimonial */
.testimonial{position:absolute;left:0;top:1560px;width:1200px;height:356px;background:linear-gradient(100deg,#ee5a25 0%,#e8462a 45%,#e12a2c 100%)}
.avatar{position:absolute;border-radius:50%;background:var(--paper);box-shadow:0 2px 6px rgba(0,0,0,.3)}
.avatar i{position:absolute;inset:6px;border-radius:50%;background:linear-gradient(160deg,#c7c7c7,#8a8a8a)}
.avatar.current i{background:linear-gradient(160deg,#6b7f99,#2e3a4b)}
.quote{position:absolute;left:260px;top:118px;width:680px;text-align:center;color:var(--paper);font-size:17px;font-style:italic;font-weight:300;line-height:24px}
.author{position:absolute;left:0;top:270px;width:1200px;text-align:center;color:var(--paper)}
.author b{display:block;font-size:11px;font-weight:700;letter-spacing:.5px}
.author span{font-size:10px}

/* partners */
.partner-card{position:absolute;left:232px;top:2036px;width:736px;height:312px;background:#f4f4f4}
.partner-photo{position:absolute;left:0;top:0;width:280px;height:312px;background:linear-gradient(135deg,#d9dde3 0%,#a8b0bb 50%,#3b4250 100%)}
.partner-body{position:absolute;left:312px;top:26px;width:380px}
.partner-body h3{font-size:31px;font-weight:300;color:var(--black);line-height:40px}
.partner-body .org{font-size:12px;font-weight:700;margin-top:2px}
.partner-body p{font-size:12px;line-height:20px;color:var(--grey);margin-top:20px}
.read-more{display:flex;align-items:center;gap:10px;font-size:12px;font-weight:600;margin-top:14px}
.partner-pager{position:absolute;left:280px;bottom:0;width:456px;height:32px;background:#7a7a7a;display:flex;justify-content:center;align-items:center;gap:8px}
.partner-pager span{width:5px;height:5px;border-radius:50%;background:var(--paper)}
.partner-pager span.on{width:10px;height:10px;background:none;border:2px solid var(--paper)}

/* footer */
.footer{position:absolute;left:0;top:2414px;width:1200px;height:506px;background:var(--light)}
.footer-shape{position:absolute;left:0;top:0}
.footer h4{position:absolute;font-size:20px;font-weight:400}
.contact-info{position:absolute;left:158px;top:98px;width:380px;color:#a9a9a9;font-size:12px;line-height:16px}
.contact-info .label{color:var(--paper);font-weight:600;margin-top:22px}
.contact-info .phone{color:var(--paper);font-size:20px;line-height:26px}
.contact-info a{color:var(--red)}
.social{position:absolute;left:158px;top:380px;color:var(--paper);font-size:12px;font-weight:600}
.social .icons{display:flex;gap:6px;margin-top:6px}
.social .icons i{width:20px;height:20px;background:#a9a9a9;border-radius:3px}
.field{position:absolute;left:692px;width:358px;height:32px;background:var(--paper);border:1px solid #c9c9c9;font-size:11px;color:var(--grey);padding:8px 10px}
.send{position:absolute;left:692px;top:408px;width:120px;height:32px;background:var(--red);color:var(--paper);font-size:12px;font-weight:700;display:flex;align-items:center;justify-content:center;gap:8px}

.legal{position:absolute;left:0;top:2920px;width:1200px;height:60px;background:var(--paper);font-size:12px;color:var(--grey)}
.legal .copy{position:absolute;left:158px;top:22px}
.legal .copy span{color:var(--red)}
.legal .links{position:absolute;left:496px;top:22px;display:flex;gap:10px}
.legal .to-top{position:absolute;left:1028px;top:18px}
</style>
</head>
<body>

<header class="site-header">
  <div class="brand">VARNOLIX</div>
  <nav class="main-nav">
    <span>Natural Intelligence</span>
    <span class="active">Products</span>
    <span>Services</span>
    <span>Partners</span>
    <span>Contact Us</span>
    <span>About</span>
  </nav>
  <div class="lang">
    <svg width="12" height="12" viewBox="0 0 12 12"><circle cx="6" cy="6" r="5.5" fill="#555"/></svg>
    English
    <svg width="8" height="6" viewBox="0 0 8 6"><path d="M0 0h8L4 5z" fill="#333"/></svg>
  </div>
</header>

<div class="submenu">
  <div>Implementation Services</div>
  <div>Business Consulting</div>
</div>

<section class="hero" role="img" aria-label="Contact center agent wearing a headset, smiling, with colleagues softly blurred behind">
  <div class="hero-strip">→ &nbsp; To promote our software products to potential customers ...</div>
  <h1 class="hero-title">Quillet, by Varnolix. The new standard in contact<br>center customer experience.</h1>
  <div class="hero-actions">
    <div class="action demo">
      <svg width="30" height="26" viewBox="0 0 30 26" fill="none" stroke="#fff" stroke-width="1.6"><path d="M2 2v22h26"/><path d="M6 18l6-7 5 4 9-10"/></svg>
      REQUEST A DEMO
    </div>
    <div class="action contact">
      <svg width="26" height="26" viewBox="0 0 26 26" fill="none" stroke="#fff" stroke-width="1.6"><path d="M6 3l4 5-2.5 2.5c1.5 3.5 4.5 6.5 8 8L18 16l5 4-3 4C11 22 4 15 2 6z"/><path d="M15 4a8 8 0 0 1 7 7M15 8a4 4 0 0 1 3 3"/></svg>
      CONTACT US
    </div>
    <div class="action partners">
      <svg width="30" height="26" viewBox="0 0 30 26" fill="none" stroke="#fff" stroke-width="1.6"><circle cx="13" cy="8" r="6"/><path d="M2 25c0-6 5-9 11-9s11 3 11 9z"/><path d="M20 3a6 6 0 0 1 0 10M24 16c3 1 5 4 5 8"/></svg>
      PARTNERS
    </div>
  </div>
</section>

<h2 class="section-title" style="top:580px">Recent News</h2>

<!-- row 1 -->
<article class="tile" style="left:232px;top:624px;width:432px;height:256px">
  <div class="art" role="img" aria-label="Grey business photo behind the ROI calculator headline" style="background:linear-gradient(135deg,#9a9a9a,#676767)"></div>
  <div class="big" style="left:114px;top:46px;font-size:98px;font-weight:400">ROI</div>
  <div class="caption">Calculate Your Omnichannel Engagement<br>Center ROI!</div>
  <svg class="more" width="30" height="30" viewBox="0 0 30 30" fill="none" stroke="#fff" stroke-width="1.5"><circle cx="15" cy="15" r="13"/><path d="M13 9l6 6-6 6"/></svg>
</article>
<article class="tile" style="left:688px;top:624px;width:280px;height:256px">
  <div class="art" role="img" aria-label="Grey office photo behind the leader award headline" style="background:linear-gradient(135deg,#8f8f8f,#5d5d5d)"></div>
  <div class="big" style="left:26px;top:40px;font-size:98px;font-weight:700">2</div>
  <div class="big" style="left:108px;top:60px;font-size:20px;line-height:28px">LEADER IN<br><b style="font-weight:600;font-size:25px">NORTHVANE<br>WAVES</b></div>
  <div class="caption">Northvane Waves:<br>CCIM for Contact Center</div>
  <svg class="more" width="30" height="30" viewBox="0 0 30 30" fill="none" stroke="#fff" stroke-width="1.5"><circle cx="15" cy="15" r="13"/><path d="M13 9l6 6-6 6"/></svg>
</article>

<!-- row 2 -->
<article class="tile" style="left:232px;top:904px;width:204px;height:256px">
  <div class="art" role="img" aria-label="Grey photo of a person at work behind a rising trend line" style="background:linear-gradient(135deg,#a0a0a0,#6a6a6a)"></div>
  <svg class="abs" style="left:0;top:30px" width="204" height="60" viewBox="0 0 204 60" fill="none" stroke="#fff" stroke-width="2"><path d="M0 50l30-20 30 14 35-30 30 18 30-26 49 20"/></svg>
  <div class="big" style="left:20px;top:98px;font-size:26px;line-height:28px">WHAT'S<br><b style="font-weight:700">TRENDING</b></div>
  <div class="caption">The Future of<br>Customer Service</div>
  <svg class="more" width="30" height="30" viewBox="0 0 30 30" fill="none" stroke="#fff" stroke-width="1.5"><circle cx="15" cy="15" r="13"/><path d="M13 9l6 6-6 6"/></svg>
</article>
<article class="tile feature" style="left:460px;top:904px;width:282px;height:256px">
  <h3>Harlow &amp; Pike:<br>When CRM Meets the Contact Center</h3>
  <p>Learn About the Benefits of Integrating Your CRM and Contact Center - with an Outline for Success ...</p>
  <div class="cta">
    <svg width="24" height="24" viewBox="0 0 24 24" fill="none" stroke="#ec1f27" stroke-width="1.5"><circle cx="12" cy="12" r="10.5"/><path d="M10 7l5 5-5 5"/></svg>
    Get Started
  </div>
</article>
<article class="tile" style="left:766px;top:904px;width:202px;height:256px">
  <div class="art" role="img" aria-label="Grey photo of a person at a desk" style="background:linear-gradient(135deg,#9c9c9c,#6a6a6a)"></div>
  <div class="big" style="left:46px;top:70px;font-size:26px;line-height:28px;text-align:center">WHAT'S<br><b style="font-weight:700">TRENDING</b></div>
  <div class="caption">The Future of<br>Customer Service</div>
  <svg class="more" width="30" height="30" viewBox="0 0 30 30" fill="none" stroke="#fff" stroke-width="1.5"><circle cx="15" cy="15" r="13"/><path d="M13 9l6 6-6 6"/></svg>
</article>

<!-- row 3 -->
<article class="tile" style="left:232px;top:1184px;width:280px;height:256px">
  <div class="art" role="img" aria-label="Grey photo behind the years as a leader headline" style="background:linear-gradient(135deg,#8c8c8c,#5a5a5a)"></div>
  <div class="big" style="left:28px;top:44px;font-size:104px;font-weight:700">8</div>
  <div class="big" style="left:122px;top:68px;font-size:24px;font-weight:700;line-height:28px">YEARS AS<br>A LEADER</div>
  <div class="caption">Corvinus Named a Leader:<br>2016 Leaders Grid</div>
  <svg class="more" width="30" height="30" viewBox="0 0 30 30" fill="none" stroke="#fff" stroke-width="1.5"><circle cx="15" cy="15" r="13"/><path d="M13 9l6 6-6 6"/></svg>
</article>
<article class="tile" style="left:536px;top:1184px;width:432px;height:256px">
  <div class="art" role="img" aria-label="Grey photo of a contact center team behind the capabilities headline" style="background:linear-gradient(135deg,#979797,#626262)"></div>
  <div class="big" style="left:114px;top:38px;font-size:38px;line-height:40px">SCORES</div>
  <div class="big" style="left:114px;top:80px;font-size:28px;font-weight:700;line-height:30px">HIGHEST IN</div>
  <div class="big" style="left:114px;top:112px;font-size:12px;font-weight:700;line-height:15px">CUSTOMER ENGAGEMENT<br>CENTER CAPABILITIES</div>
  <div class="caption">Brightmark:<br>Critical Capabilities for Contact Centers</div>
  <svg class="more" width="30" height="30" viewBox="0 0 30 30" fill="none" stroke="#fff" stroke-width="1.5"><circle cx="15" cy="15" r="13"/><path d="M13 9l6 6-6 6"/></svg>
</article>

<!-- testimonial -->
<section class="testimonial" role="img" aria-label="Red and orange low-poly background behind a client testimonial">
  <svg class="abs" style="left:170px;top:152px" width="20" height="40" viewBox="0 0 20 40" fill="none" stroke="#fff" stroke-width="2"><path d="M18 2L2 20l16 18"/></svg>
  <svg class="abs" style="left:1010px;top:152px" width="20" height="40" viewBox="0 0 20 40" fill="none" stroke="#fff" stroke-width="2"><path d="M2 2l16 18L2 38"/></svg>
  <p class="quote">"It has survived not only five centuries, but also the leap into electronic typesetting, remaining essentially unchanged. It was popularised in the 1960s with the release of Letraset sheets containing Lorem Ipsum passages, and more recently with desktop publishing software."</p>
  <svg class="abs" style="left:588px;top:236px" width="24" height="24" viewBox="0 0 24 24"><circle cx="12" cy="12" r="11" fill="#fff"/></svg>
  <div class="author"><b>MIRA CASTELL</b><span>CEO, Studio Nine</span></div>
</section>
<div class="avatar" style="left:410px;top:1514px;width:104px;height:104px" role="img" aria-label="Client portrait"><i></i></div>
<svg class="abs" style="left:580px;top:1616px" width="40" height="22" viewBox="0 0 40 22"><path d="M0 0h40L20 22z" fill="#fff"/></svg>
<div class="avatar current" style="left:544px;top:1506px;width:112px;height:112px" role="img" aria-label="Portrait of the quoted client"><i></i></div>
<div class="avatar" style="left:686px;top:1514px;width:104px;height:104px" role="img" aria-label="Client portrait"><i></i></div>

<!-- partners -->
<h2 class="section-title" style="top:1982px"><span><span class="brand-word">VARNOLIX</span> Partners</span></h2>
<section class="partner-card">
  <div class="partner-photo" role="img" aria-label="Smiling businessman in a suit with colleagues at a meeting table behind him"></div>
  <div class="partner-body">
    <h3>Dean Holloway,</h3>
    <div class="org">Keystone Web</div>
    <p>It is a long established fact that a reader will be distracted by the readable content of a page when looking at its layout of using Lorem Ipsum is that it has a more-or-less normal distribution of letters, as opposed to using 'Content here, content here', making it look like readable English.</p>
    <div class="read-more">
      <svg width="26" height="26" viewBox="0 0 26 26" fill="none" stroke="#333" stroke-width="1.5"><circle cx="13" cy="13" r="11.5"/><path d="M11 8l5 5-5 5"/></svg>
      Read More
    </div>
  </div>
  <div class="partner-pager"><span></span><span></span><span class="on"></span><span></span><span></span></div>
</section>

<!-- footer -->
<footer class="footer">
  <svg class="footer-shape" width="700" height="506" viewBox="0 0 700 506">
    <path d="M0 0H602V150C602 185 640 210 640 256C640 302 602 327 602 362V506H0Z" fill="#231f20"/>
    <path d="M616 248l8 8-8 8" fill="none" stroke="#fff" stroke-width="2"/>
  </svg>
  <h4 style="left:158px;top:74px;color:#fff">Contact Info</h4>
  <div class="contact-info">
    <div>Varnolix Canada Corp.<br>18 Alder Row, #310 Toronto, ON Canada M4T 2K8</div>
    <div class="label">Phone:</div>
    <div class="phone">800 555 0142</div>
    <div class="label">Email:</div>
    <div><a>info@varnolix.com</a></div>
    <div style="margin-top:22px">For HR inquiries, please use<br>careers@varnolix.com</div>
  </div>
  <div class="social">Get Social:
    <div class="icons"><i></i><i></i><i></i><i></i><i></i></div>
  </div>

  <h4 style="left:692px;top:74px;color:#222">Drop A Line</h4>
  <div class="field" style="top:128px">Your Name*</div>
  <div class="field" style="top:178px">Enter your Email*</div>
  <div class="field" style="top:228px">Subject</div>
  <div class="field" style="top:278px;height:96px">Type your Message ...</div>
  <div class="send">
    <svg width="14" height="12" viewBox="0 0 14 12"><path d="M0 5L14 0 10 12 7 7z" fill="#fff"/></svg>
    SEND
  </div>
</footer>

<div class="legal">
  <div class="copy">© 2016 <span>Varnolix Canada Corp.</span> All rights reserved.</div>
  <div class="links"><span>Sitemap</span>|<span>Terms of Use</span>|<span>Privacy Policy</span>|<span>Careers</span></div>
  <svg class="to-top" width="22" height="22" viewBox="0 0 22 22"><circle cx="11" cy="11" r="11" fill="#ec1f27"/><path d="M6 12l5-5 5 5M11 7v9" fill="none" stroke="#fff" stroke-width="2"/></svg>
</div>

</body>
</html>
```